Designing our 2018 Look Book! New help with slide design and picture layout

We create a yearly "Look book" with all of our season's designs for the year and need creative help creating the design and layout of the book

Need help with the slide design and picture layout

Target Market(s)

Property managers and office managers

Requirements
Must have
• layout of the photos and design of cover slide templates
• See our logo attached (color scheme and you can use the logo as well)
• Also see our website for our "look" www.dunvoria.com

```html
<!DOCTYPE html>
<html lang="en">
<head>
<meta charset="utf-8">
<title>Dunvoria – Growth Hackers cover</title>
<link href="https://fonts.googleapis.com/css2?family=Work+Sans:wght@400;500;600&display=swap" rel="stylesheet">
<style>
  :root {
    --backdrop: #a9a8a8;
    --paper: #ffffff;
    --leaf-green: #78a83a;
    --deep-green: #5f8f2a;
    --panel-green: rgba(108, 150, 60, 0.92);
    --soft-green: #8dae62;
    --slate: rgba(90, 92, 94, 0.75);
    --ink-white: #ffffff;
  }
  html, body {
    margin: 0;
    padding: 0;
    width: 1200px;
    height: 789px;
    overflow: hidden;
    background: var(--backdrop);
    font-family: "Work Sans", Arial, sans-serif;
  }
  .canvas {
    position: relative;
    width: 1200px;
    height: 789px;
  }
  .cover {
    position: absolute;
    left: 338px;
    top: 24px;
    width: 524px;
    height: 741px;
    background: var(--paper);
    overflow: hidden;
    box-shadow: 0 6px 18px rgba(0,0,0,0.25);
  }
  .cover__rule {
    position: absolute;
    left: 0; top: 0;
    width: 100%;
    height: 5px;
    background: var(--leaf-green);
  }
  .brand {
    position: absolute;
    left: 0; top: 86px;
    width: 100%;
    display: flex;
    justify-content: center;
    align-items: center;
    gap: 12px;
  }
  .brand__dot {
    width: 18px; height: 18px;
    border-radius: 50%;
    background: var(--leaf-green);
  }
  .brand__name {
    font-size: 48px;
    font-weight: 500;
    color: var(--leaf-green);
    letter-spacing: 0.5px;
  }
  .cover__photo {
    position: absolute;
    left: 0; top: 178px;
    width: 100%;
    height: 385px;
    background: linear-gradient(180deg, #f3f4f4 0%, #e6e8e8 45%, #9c9fa2 72%, #7a6a5c 100%);
  }
  .accent-square {
    position: absolute;
    left: 292px; top: 537px;
    width: 44px; height: 44px;
    background: var(--slate);
  }
  .headline {
    position: absolute;
    left: 38px; top: 525px;
    width: 254px;
    padding: 10px 14px 8px;
    box-sizing: border-box;
    background: var(--panel-green);
    color: var(--ink-white);
    font-size: 22px;
    font-weight: 600;
  }
  .tagline {
    position: absolute;
    left: 38px; top: 566px;
    width: 254px;
    padding: 10px 14px 14px;
    box-sizing: border-box;
    background: var(--soft-green);
    color: var(--ink-white);
    font-size: 17px;
    font-weight: 400;
    line-height: 1.3;
  }
  .web-bar {
    position: absolute;
    right: 0; top: 680px;
    width: 208px;
    height: 28px;
    background: var(--deep-green);
    color: var(--ink-white);
    display: flex;
    align-items: center;
    padding-left: 12px;
    box-sizing: border-box;
    gap: 6px;
    font-size: 16px;
  }
  .web-bar__dot {
    width: 7px; height: 7px;
    border-radius: 50%;
    background: var(--ink-white);
  }
  .web-bar strong { font-weight: 600; }
</style>
</head>
<body>
<div class="canvas">
  <section class="cover">
    <div class="cover__rule"></div>
    <header class="brand">
      <span class="brand__dot"></span>
      <span class="brand__name">Dunvoria</span>
    </header>
    <div class="cover__photo" role="img" aria-label="Bright white meeting room with a long white table, grey chairs, potted succulents and tall black-framed windows"></div>
    <div class="accent-square"></div>
    <h1 class="headline" style="margin:0">Growth Hackers</h1>
    <p class="tagline" style="margin:0">Create a healthy, productive workplace through plants.</p>
    <div class="web-bar"><span class="web-bar__dot"></span><span>www.<strong>dunvoria</strong>.com</span></div>
  </section>
</div>
</body>
</html>
```